Try-fold Brochure for a Dried Fruits and Nuts Retail Shop

Toranj Bazaar, is a chain of retail shops in Kabul Afghanistan. The business serves high quality dried fruits, Nuts, and a small amount of sweets. The company strive to provide the market (unlike others) a quality product that is graded and sort before packing. Its products are clean, without elements like stones, dusks, or leaves. Toranj Bazaar is a multi-unit retail that will be supported by a dry fruits and nuts processing plants in the near future. The sign of Toranj Bazaar is attached. The sign of the parent company Meridane Works & Building Provisions is attached, however, the wording on the name will be changed to Meridane Works Afghanistan while keeping the circular round logo.

The brochure to focus on the health aspect of dry fruits and nuts along with pictures for Almonds, Walnuts, Pistachios, dry apricots, and raisins for example. The colour scheme to be earth tone colours. Hope this helps. The final product also must allow me to enter texts in Farsi as well as English.
Updates

Greetings everyone, Please see additional notes, description I posted this morning. Good luck and best wishes. Farid

Reason: The designs in the recent days are getting better. I am also traveling at the moment so an other five days of extension I think would help everyone. Thank you very much for all your submissions so far. I think we are getting near to select an awesome design. Thanks again. Farid

Target Market(s)

Retail markets in Afghanistan, wholesale traders in India, the UAE, Far East for now, Europe/US/Canda markets in three years.

Industry/Entity Type

Retail

Font styles to use
Serif
Sans Serif

Colors
fdf9cf
cadf82
85cae6
fbed23
fde3d4

Requirements
Must have
• It would be good to know that Afghanistan's fruits and nuts are sought after globally and is the rarest, tastiest fruits and nuts in the world. What it lacks is proper processing to include sorting, grading, cleaning and professional packaging. Toranj Bazaars aim here is to do exactly what this market is missing. Through its processing plant own by its parent company Meridane Works Afghanistan, the company aims to offer the Afghan dry fruits and nuts to the market with all international standards for quality, safety, proper processing and professional packaging at its plant just outside of Kabul, Afghanistan.
Nice to have
• Whenever pictures of nuts used, it would be great to have some benefits of that particular item. For instance, if you have pictures of Almond, the write the benefits of Almonds. I would like to have Almonds, Walnuts, Pistachios, and i.e., dry figs, dried apricots, raisins, etc. When using pictures, I would like them to be transposed in such a way that the covers of the pictures are not visible. Also, please leave one half of one of the folds in the outside for list of addresses and phone numbers of our locations in Kabul, Afghanistan. Currently, there will be five addresses to be entered.

All our stores are designed better than any other retail shop in Kabul. The standard of design and carpentry workmanship is to the same level of quality work one would fine in the US and Europe. Hope this helps.

Elegant, colourful, modern, bold to state a statement of quality.

```html
<!DOCTYPE html>
<html lang="en">
<head>
<meta charset="utf-8">
<title>Toranj Bazaar – Tri-fold Brochure</title>
<link rel="stylesheet" href="https://fonts.googleapis.com/css2?family=Open+Sans:wght@400;600;700&family=Lalezar&family=Vazirmatn:wght@700&display=swap">
<style>
  :root {
    --ink-light: #ffffff;
    --accent-lime: #b9d437;
    --accent-yellow: #d8e04a;
    --earth-dark: #33241a;
    --earth-mid: #6b4a22;
    --moss: #4f5c43;
    --moss-dark: #2f3a2e;
    --band: rgba(255, 255, 255, 0.16);
    --fold-line: rgba(255, 255, 255, 0.9);
  }
  * { box-sizing: border-box; margin: 0; padding: 0; }
  html, body { width: 1200px; height: 848px; overflow: hidden; background: #ffffff; }
  .brochure {
    position: relative;
    width: 1200px;
    height: 848px;
    overflow: hidden;
    font-family: "Open Sans", Arial, sans-serif;
    color: var(--ink-light);
    background:
      radial-gradient(ellipse 520px 380px at 600px 440px, rgba(245, 200, 90, 0.95), rgba(233, 184, 74, 0) 100%),
      linear-gradient(180deg, var(--earth-dark) 0%, var(--earth-mid) 22%, #9a7430 42%, #8a8a4a 60%, var(--moss) 78%, var(--moss-dark) 100%);
  }
  .band { position: absolute; background: var(--band); }
  .band--top { left: 0; top: 256px; width: 1200px; height: 79px; }
  .band--center { left: 400px; top: 638px; width: 400px; height: 160px; }
  .fold-line {
    position: absolute; top: 0; width: 0; height: 848px;
    border-left: 2px dashed var(--fold-line);
  }
  .fold-line--one { left: 399px; }
  .fold-line--two { left: 799px; }

  .brand-en {
    position: absolute; left: 12px; top: 40px;
    font-size: 44px; font-weight: 600; letter-spacing: 0.3px; line-height: 1;
  }
  .tagline-en {
    position: absolute; left: 22px; top: 132px;
    font-size: 16px; font-weight: 700; color: var(--accent-lime);
  }
  .brand-fa {
    position: absolute; right: 22px; top: 20px;
    font-family: "Lalezar", "Vazirmatn", sans-serif;
    font-size: 62px; line-height: 1.1; direction: rtl;
  }
  .tagline-fa {
    position: absolute; right: 38px; top: 130px;
    font-family: "Vazirmatn", sans-serif; font-weight: 700;
    font-size: 16px; color: var(--accent-yellow); direction: rtl;
  }

  .photo-disc { position: absolute; }
  .photo-disc--pistachio { left: 80px; top: 232px; }
  .photo-disc--walnut { left: 884px; top: 224px; }
  .photo-disc--almond { left: 473px; top: 570px; }

  .parent-mark {
    position: absolute; left: 460px; top: 50px; width: 280px;
    text-align: center;
  }
  .parent-mark__dot {
    display: block; width: 110px; height: 110px; margin: 0 auto 8px;
    border-radius: 50%; background: var(--ink-light);
  }
  .parent-mark__name { font-size: 16px; font-weight: 600; }

  .body-copy {
    position: absolute;
    font-size: 21px; line-height: 34.5px;
    text-align: justify; hyphens: auto; -webkit-hyphens: auto;
  }
  .body-copy strong { font-weight: 700; color: var(--accent-yellow); }
  .body-copy--left { left: 23px; top: 484px; width: 356px; }
  .body-copy--center { left: 422px; top: 252px; width: 356px; }
  .body-copy--right { left: 825px; top: 484px; width: 354px; }
</style>
</head>
<body>
<main class="brochure">
  <div class="band band--top"></div>
  <div class="band band--center"></div>
  <div class="fold-line fold-line--one"></div>
  <div class="fold-line fold-line--two"></div>

  <section class="panel panel--left">
    <h1 class="brand-en">TORANJ BAZAAR</h1>
    <p class="tagline-en">Provider of Dried Fruits, Nuts and Sweets</p>
    <svg class="photo-disc photo-disc--pistachio" width="228" height="228" viewBox="0 0 228 228" role="img" aria-label="Photo of roasted pistachios in their shells with green leaves">
      <defs>
        <radialGradient id="pistachioTone" cx="50%" cy="50%" r="50%">
          <stop offset="0%" stop-color="#d9c08a"/>
          <stop offset="55%" stop-color="#efe3c4"/>
          <stop offset="100%" stop-color="#ffffff"/>
        </radialGradient>
      </defs>
      <circle cx="114" cy="114" r="114" fill="url(#pistachioTone)"/>
    </svg>
    <p class="body-copy body-copy--left"><strong>Pistachios</strong> are rich in protein, fibre and antioxidants that support a healthy heart and steady blood sugar. Their lutein protects the eyes and vitamin B6 helps the blood and nerves. Every Afghan pistachio we pack is graded and cleaned, free of stones, dust and leaves.</p>
  </section>

  <section class="panel panel--center">
    <div class="parent-mark">
      <span class="parent-mark__dot"></span>
      <span class="parent-mark__name">Meridane Works Afghanistan</span>
    </div>
    <p class="body-copy body-copy--center">Afghan dried fruits and nuts are among the rarest and tastiest in the world. We sort, grade, clean and pack them to international standards at our plant near Kabul. Visit our stores in Shahr-e Naw, Karte Se, Wazir Akbar Khan, Macroyan and Taimani.</p>
    <svg class="photo-disc photo-disc--almond" width="242" height="242" viewBox="0 0 242 242" role="img" aria-label="Photo of whole almonds with a green leaf">
      <defs>
        <radialGradient id="almondTone" cx="50%" cy="50%" r="50%">
          <stop offset="0%" stop-color="#b9773f"/>
          <stop offset="55%" stop-color="#e8cfb2"/>
          <stop offset="100%" stop-color="#ffffff"/>
        </radialGradient>
      </defs>
      <circle cx="121" cy="121" r="121" fill="url(#almondTone)"/>
    </svg>
  </section>

  <section class="panel panel--right">
    <h2 class="brand-fa" lang="fa">بازار ترنج</h2>
    <p class="tagline-fa" lang="fa">عرضه کننده انواع میوه خشک و شیرینی</p>
    <svg class="photo-disc photo-disc--walnut" width="228" height="228" viewBox="0 0 228 228" role="img" aria-label="Photo of walnuts, whole and cracked, with a green leaf">
      <defs>
        <radialGradient id="walnutTone" cx="50%" cy="50%" r="50%">
          <stop offset="0%" stop-color="#a87a4c"/>
          <stop offset="55%" stop-color="#e6d3bd"/>
          <stop offset="100%" stop-color="#ffffff"/>
        </radialGradient>
      </defs>
      <circle cx="114" cy="114" r="114" fill="url(#walnutTone)"/>
    </svg>
    <p class="body-copy body-copy--right"><strong>Walnuts</strong> are the richest nut in plant omega-3 fats, supporting brain health and memory and helping lower bad cholesterol. Their polyphenols calm inflammation and magnesium keeps muscles working well. Ours are hand-sorted so only clean, whole kernels reach you.</p>
  </section>
</main>
</body>
</html>
```